Business Card Design

New business card design

Target Market(s)

Residential & Commercial Property Managers

Industry/Entity Type

Plumbing Services

Contact Information for Business Card

Name - Owen Tredgold, title - Director, Phone Number - 0431 862 507, email - owen@rvb-plumbing.com.au, Company ABN - 73 215 904 386,

Font styles to use
Sans Serif

Colors
0054AA
0677BA
7BADD7
CADEEF
E8F1F8

```html
<!DOCTYPE html>
<html lang="en">
<head>
<meta charset="utf-8">
<title>RVB Plumbing Services – Business Card</title>
<link rel="stylesheet" href="https://fonts.googleapis.com/css2?family=Lato:wght@300;400;700;900&display=swap">
<style>
  :root {
    --blue-deep: #0054AA;
    --blue-mid: #0677BA;
    --blue-bright: #1BA8E6;
    --blue-light: #7BADD7;
    --blue-pale: #CADEEF;
    --blue-mist: #E8F1F8;
    --ink: #1B2230;
    --paper: #FFFFFF;
    --backdrop: #2A2D33;
  }
  * { box-sizing: border-box; margin: 0; padding: 0; }
  html, body {
    width: 1200px; height: 875px; overflow: hidden;
    background: var(--backdrop);
    font-family: "Lato", sans-serif;
  }
  .sheet {
    width: 1200px; height: 875px;
    display: flex; flex-direction: column;
    align-items: center; justify-content: center; gap: 50px;
  }
  .card {
    position: relative;
    width: 630px; height: 360px;
    border-radius: 22px;
    overflow: hidden;
    box-shadow: 0 14px 34px rgba(0,0,0,.45);
  }

  /* Front */
  .card-front .wave-field {
    position: absolute; inset: 0;
    background:
      linear-gradient(160deg, #6FE0F8 0%, #35C6F2 30%, var(--blue-bright) 55%, var(--blue-mid) 80%, var(--blue-deep) 100%);
  }
  .card-front .brand {
    position: absolute; left: 0; right: 0; top: 50%;
    transform: translateY(-50%);
    text-align: center; color: var(--paper);
    font-weight: 300;
  }
  .brand-name { font-size: 96px; letter-spacing: 6px; line-height: 1; }
  .brand-tag { font-size: 15px; letter-spacing: 11px; margin-top: 12px; text-transform: lowercase; }

  /* Back */
  .card-back { background: var(--paper); }
  .card-back .edge-arcs { position: absolute; inset: 0; }
  .back-layout {
    position: absolute; inset: 0;
    display: flex; align-items: center;
    padding: 0 60px 0 70px;
  }
  .back-brand {
    width: 250px; text-align: center; color: var(--ink); font-weight: 300;
  }
  .back-brand .brand-name { font-size: 66px; letter-spacing: 4px; }
  .back-brand .brand-tag { font-size: 11px; letter-spacing: 7px; margin-top: 10px; }
  .divider {
    width: 2px; height: 150px; background: var(--blue-bright);
    margin: 0 34px 0 26px;
  }
  .contact { color: var(--ink); }
  .contact-name {
    font-weight: 900; font-size: 27px; color: var(--blue-bright);
    text-transform: uppercase; letter-spacing: .5px; line-height: 1.05;
  }
  .contact-role { font-weight: 700; font-size: 16px; margin: 4px 0 14px; }
  .contact-list { list-style: none; font-size: 14.5px; line-height: 1.65; }
  .contact-list li { display: flex; align-items: center; gap: 8px; }
  .contact-list svg { width: 13px; height: 13px; flex: none; }
  .contact-list .abn { padding-left: 21px; }
</style>
</head>
<body>
<main class="sheet">

  <section class="card card-front" aria-label="Business card front">
    <div class="wave-field" role="img" aria-label="Layered blue water-wave background"></div>
    <div class="brand">
      <div class="brand-name">RVB</div>
      <div class="brand-tag">plumbing services</div>
    </div>
  </section>

  <section class="card card-back" aria-label="Business card back">
    <svg class="edge-arcs" viewBox="0 0 630 360" aria-hidden="true">
      <path d="M150 12 A168 168 0 0 0 150 348" fill="none" stroke="var(--blue-bright)" stroke-width="4"/>
      <path d="M480 12 A168 168 0 0 1 480 348" fill="none" stroke="var(--blue-bright)" stroke-width="4"/>
    </svg>
    <div class="back-layout">
      <div class="back-brand">
        <div class="brand-name">RVB</div>
        <div class="brand-tag">plumbing services</div>
      </div>
      <div class="divider"></div>
      <div class="contact">
        <div class="contact-name">Owen Tredgold</div>
        <div class="contact-role">Director</div>
        <ul class="contact-list">
          <li>
            <svg viewBox="0 0 24 24" aria-hidden="true"><path fill="var(--blue-bright)" d="M6.6 10.8a15 15 0 0 0 6.6 6.6l2.2-2.2a1 1 0 0 1 1-.25 11.4 11.4 0 0 0 3.6.57 1 1 0 0 1 1 1V20a1 1 0 0 1-1 1A17 17 0 0 1 3 4a1 1 0 0 1 1-1h3.5a1 1 0 0 1 1 1c0 1.25.2 2.45.57 3.6a1 1 0 0 1-.25 1z"/></svg>
            0431 862 507
          </li>
          <li>
            <svg viewBox="0 0 24 24" aria-hidden="true"><rect x="2" y="5" width="20" height="14" rx="2" fill="var(--blue-bright)"/><path d="M3 6l9 7 9-7" fill="none" stroke="#fff" stroke-width="2"/></svg>
            owen@rvb-plumbing.com.au
          </li>
          <li class="abn">ABN - 73 215 904 386</li>
        </ul>
      </div>
    </div>
  </section>

</main>
</body>
</html>
```